Road Construction Company needs business cards

We would like a new business card designed for our business.

We're a road construction company based in Qld, Australia.

Can the business card please have the following information on it.

Name: Brent Malvoy
Position: General Manager
Phone: 0471 592 304
Email: Brent.malvoy@quendix.com.au
Address: 87 Harrowgate Ave, Pindarra, QLD, 4000
Website: www.quendix.com.au

Visually we'd like the card to be professional and simple.

Attached is our logo.

Our website is www.quendix.com.au

Target Market(s)

Men aged 25-60

Contact Information for Business Card

As listed in project description

Font styles to use
Serif

Requirements
Must have
• Large logo on back of card

```html
<!DOCTYPE html>
<html lang="en">
<head>
<meta charset="utf-8">
<title>Quendix Business Card</title>
<link href="https://fonts.googleapis.com/css2?family=Source+Serif+4:wght@400;700&display=swap" rel="stylesheet">
<style>
  :root {
    --blue: #0a3ff2;
    --cyan: #4dcff4;
    --paper: #ffffff;
    --backdrop: #ffffff;
  }
  * { margin: 0; padding: 0; box-sizing: border-box; }
  html, body {
    width: 996px; height: 1200px; overflow: hidden;
    background: var(--backdrop);
    font-family: "Source Serif 4", Georgia, serif;
  }
  .card {
    position: absolute; left: 48px; width: 900px; height: 500px;
    background: var(--paper);
    box-shadow: 0 6px 22px rgba(0,0,0,0.28);
    overflow: hidden;
  }
  .card--front { top: 87px; }
  .card--back { top: 631px; }

  .holder-name {
    position: absolute; left: 89px; top: 78px;
    font-weight: 700; font-size: 53px; color: var(--blue); line-height: 1;
  }
  .holder-role {
    position: absolute; left: 89px; top: 156px;
    font-size: 34px; color: var(--cyan); line-height: 1;
  }
  .contact-list {
    position: absolute; left: 87px; top: 268px; list-style: none;
  }
  .contact-list li {
    display: flex; align-items: center; height: 42.5px;
    font-size: 25px; color: var(--blue);
  }
  .contact-list svg {
    width: 28px; height: 28px; margin-right: 14px; flex: none;
    fill: none; stroke: var(--cyan); stroke-width: 1.6;
    stroke-linecap: round; stroke-linejoin: round;
  }
  .stripes { position: absolute; left: 0; top: 0; }

  .brand-name {
    position: absolute; left: 0; right: 0; top: 185px;
    text-align: center; font-weight: 700; font-size: 108px;
    letter-spacing: 4px; color: var(--blue); line-height: 1;
  }
  .back-url {
    position: absolute; left: 0; right: 0; top: 426px;
    text-align: center; font-size: 25px; color: var(--cyan);
  }
</style>
</head>
<body>
  <section class="card card--front">
    <h1 class="holder-name">Brent Malvoy</h1>
    <p class="holder-role">General Manager</p>
    <ul class="contact-list">
      <li>
        <svg viewBox="0 0 24 24"><path d="M5 3h4l2 5-2.5 1.5a11 11 0 0 0 6 6L16 13l5 2v4a2 2 0 0 1-2 2A16 16 0 0 1 3 5a2 2 0 0 1 2-2z"/><path d="M15 3a6 6 0 0 1 6 6M15 7a2 2 0 0 1 2 2"/></svg>
        0471 592 304
      </li>
      <li>
        <svg viewBox="0 0 24 24"><path d="M3 10l9-7 9 7v11H3z"/><path d="M3 10l9 6 9-6"/><circle cx="12" cy="9" r="2.5"/></svg>
        Brent.malvoy@quendix.com.au
      </li>
      <li>
        <svg viewBox="0 0 24 24"><path d="M2 12L12 3l10 9"/><path d="M5 10v11h14V10"/><path d="M10 21v-6h4v6"/><rect x="10" y="8" width="4" height="3"/></svg>
        87 Harrowgate Ave, Pindarra, QLD, 4000
      </li>
      <li>
        <svg viewBox="0 0 24 24"><circle cx="12" cy="12" r="9"/><path d="M3 12h18M12 3c3 3 3 15 0 18M12 3c-3 3-3 15 0 18M5 7h14M5 17h14"/></svg>
        www.quendix.com.au
      </li>
    </ul>
    <svg class="stripes" width="900" height="500" viewBox="0 0 900 500" aria-hidden="true">
      <polygon points="796,130 900,130 900,277 790,500 608,500" fill="var(--blue)"/>
      <polygon points="900,351 900,500 828,500" fill="var(--cyan)"/>
    </svg>
  </section>

  <section class="card card--back">
    <p class="brand-name">QUENDIX</p>
    <p class="back-url">www.quendix.com.au</p>
  </section>
</body>
</html>
```